GuardVOLT Brochure

We need a new brochure designed for our GuardVOLT Unit. I have provided examples of previous and words for the new ones. Stock photos will be purchased and forwarded once design is complete.

I have also attached a competitors product brochure for reference. This is a bout conveying by using our product your people will be safe and will not need to use high rated PPE
Updates

Project Deadline Extended
Reason: Will be extending the project for 1 day and selecting the final design tomorrow to allow some of you to fine tune submissions.

Target Market(s)

Professionals

Industry/Entity Type

Product

Contact Information for Business Card

Refer Attached Details

Requirements
Must have
• Pemberton Lisle Logo and Colours Business Card
• Brochure should complement GuardVOLT Logo

```html
<!DOCTYPE html>
<html lang="en">
<head>
<meta charset="utf-8">
<title>GuardVOLT Brochure Spread</title>
<link rel="stylesheet" href="https://fonts.googleapis.com/css2?family=Open+Sans:wght@400;600&display=swap">
<style>
  :root {
    --backdrop: #d9d9d9;
    --paper: #ffffff;
    --ink: #3a3a3a;
    --brand-blue: #1f7fc1;
    --band-dark: #3b3d42;
    --band-mid: #55585e;
    --unit-orange: #d8702f;
    --unit-grey: #7a8591;
    --site-sky: #c9c6bd;
  }
  * { box-sizing: border-box; margin: 0; padding: 0; }
  html, body { width: 1200px; height: 800px; overflow: hidden; }
  body {
    background: var(--backdrop);
    font-family: "Open Sans", Arial, sans-serif;
    color: var(--ink);
    position: relative;
  }
  .spread {
    position: absolute; left: 60px; top: 40px;
    width: 1080px; height: 720px;
    background: var(--paper);
    box-shadow: 0 2px 10px rgba(0,0,0,.15);
    overflow: hidden;
  }
  .fold {
    position: absolute; left: 540px; top: 0; width: 1px; height: 100%;
    background: rgba(0,0,0,.12);
  }
  .hero-band {
    position: absolute; left: 0; top: 0; width: 100%; height: 240px;
    background: linear-gradient(100deg, var(--band-dark) 0%, var(--band-mid) 45%, var(--band-dark) 100%);
  }
  .hero-rule {
    position: absolute; left: 0; top: 240px; width: 100%; height: 2px;
    background: var(--brand-blue);
  }
  .brand {
    position: absolute; top: 26px;
    display: flex; align-items: center; gap: 8px;
    color: var(--brand-blue); font-size: 10px; font-weight: 600;
  }
  .brand-mark { width: 22px; height: 22px; background: var(--brand-blue); }
  .brand-tagline { font-weight: 400; font-size: 8px; margin-left: 10px; }
  .brand--left { left: 30px; }
  .brand--right { left: 570px; }

  .column {
    position: absolute; top: 262px;
    font-size: 8px; line-height: 1.32;
  }
  .column h2 {
    color: var(--brand-blue); font-size: 9.5px; font-weight: 400;
    padding-bottom: 3px; border-bottom: 1px solid var(--brand-blue);
    margin: 12px 0 6px; display: inline-block;
  }
  .column h2:first-child { margin-top: 0; }
  .column p { margin-bottom: 4px; }
  .column ul { list-style: none; margin-bottom: 4px; }
  .column ul li { padding-left: 9px; position: relative; }
  .column ul li::before {
    content: ""; position: absolute; left: 0; top: 3px;
    width: 5px; height: 5px; background: var(--ink);
  }
  .column ol { padding-left: 12px; margin-bottom: 4px; }
  .column--intro { left: 30px; width: 230px; }
  .column--factors { left: 285px; width: 230px; }
  .column--benefits { left: 810px; width: 245px; }

  .product-render {
    display: block; margin: 12px 0 0 15px; width: 130px; height: 100px;
    background: linear-gradient(90deg, var(--unit-orange) 0%, var(--unit-orange) 45%, var(--unit-grey) 55%, var(--unit-grey) 100%);
    border-radius: 3px;
  }
  .site-photo {
    position: absolute; left: 570px; top: 256px; width: 220px; height: 440px;
    background: linear-gradient(180deg, var(--site-sky) 0%, var(--unit-orange) 40%, #9a5a30 70%, #6f6f6a 100%);
  }
</style>
</head>
<body>
  <div class="spread">
    <div class="hero-band" role="img" aria-label="Photo of an electrical switchroom with rows of switchgear cabinets"></div>
    <div class="hero-rule"></div>
    <div class="fold"></div>

    <div class="brand brand--left">
      <span class="brand-mark"></span><span>Pemberton Lisle</span>
      <span class="brand-tagline">Technology and Innovation Improvements</span>
    </div>
    <div class="brand brand--right">
      <span class="brand-mark"></span><span>Pemberton Lisle</span>
      <span class="brand-tagline">Technology and Innovation Improvements</span>
    </div>

    <section class="column column--intro">
      <h2>The Arc Flash Problem</h2>
      <p>Electrical safety generally has been geared towards preventing electrocution with statistics indicating industry has been successful in achieving. Arc Flash is NOT an Electric Shock, it is an ELECTRICAL PLASMA EXPLOSION which is capable of severely burning personnel within the exposure area. The explosion can maim or kill within as little time as 40ms by expelling outwards from the source:</p>
      <ul>
        <li>Extreme Temperatures;</li>
        <li>Molten Metal;</li>
        <li>Toxic Gases</li>
        <li>High Pressure Wave</li>
      </ul>
      <h2>The Hazards again are:</h2>
      <ul>
        <li>Heat causes 2nd degree burns on exposed skin;</li>
        <li>Heat ignites clothing causing severe 3rd degree burns;</li>
        <li>Inhaling of molten metal and the toxic plasma plume causes lung damage;</li>
        <li>Pressure wave sound can exceed levels which can damage human ears;</li>
        <li>Pressure wave can cause personnel injury.</li>
      </ul>
      <h2>The Complacency Problem</h2>
      <p>How often have you heard, this has never happen in our facility our processes and equipment very good and will prevent this? This is a game of bravado and probability as most arc flash events are caused by:</p>
      <ol>
        <li>Human error;</li>
        <li>Equipment failure;</li>
        <li>Vermin infestation.</li>
      </ol>
      <p>Can you truly place your hand on your heart and say these events will never happens at your facility?</p>
    </section>

    <section class="column column--factors">
      <h2>What are the Severity Factors Involved?</h2>
      <p>The severity factors involved are:<br>
      1. Energy, how big is the explosion;<br>
      2. Time, how long does the explosion go for;<br>
      3. Distance, how close to the explosion will I be.<br>
      The most effective way lowing the severity of an Arc Flash Event is to reduce Energy Quickly.</p>
      <h2>Why Not Just Use Rate PPE</h2>
      <p>Providing separation and distance via PPE should be your last choice to manage this problem. Don't let the judicial system judge whether your PPE was adequate risk prevention in the event of an incident. Courts often take the view that irrespective of the numerical risk criteria, the broad aim should be to avoid risk So Far As Is Reasonably Practical (SFAIRP).</p>
      <h2>What is our Solution?</h2>
      <p>Our simple but elegant engineered high speed fuse assembly installed on the secondary (480V) side of distribution transformers. The assembly is engineered to carry normal load currents up to 3600A, but respond extremely quickly to fault currents interrupting faults within half cycle (5ms@50Hz/4ms@60Hz) and limiting arc incident energy to less than 1.2 cal/cm².</p>
      <div class="product-render" role="img" aria-label="Rendering of the GuardVOLT fuse unit, orange enclosure beside a grey transformer"></div>
    </section>

    <div class="site-photo" role="img" aria-label="Photo of an orange GuardVOLT unit installed behind a fenced transformer yard"></div>

    <section class="column column--benefits">
      <h2>Significant Benefits include</h2>
      <ol>
        <li>Protects personnel from severe burns by reducing the Arc Flash Incident Energy to less than 1.2 cal/cm² in 415/480V systems = Safer Work Environment;</li>
        <li>Enables personnel to operated 480V electrical equipment with PEE rated for less than 4 cal/cm², = More wearable and comfortable PPE clothing;</li>
        <li>Low capital cost compared to equipment replacement, = Efficient use of Scarce Capital;</li>
        <li>Can be retrofitted to any installation within 16-24 hrs, = Low Production Impact to implement;</li>
        <li>Rigorously tested at an internationally recognized Veritest test facility, = Guaranteed to Work in our certified engineered applications;</li>
        <li>System uniquely protects at the source of the energy, = Safer, Protected Assets;</li>
        <li>When it is required to operate, you will be up and running within hours not days or months = Low Production Impact from Arc Flash Safety Incident</li>
      </ol>
      <h2>Safety is Important, Need Further Proof Right?</h2>
      <p>Type testing was performed by the Veritest, NTLA certified test center located in Melbourne Victoria Australia during June 2010 through to September 2012. The testing program was conducted in accordance with:</p>
      <ul>
        <li>AS/IEC60947.1 Low Voltage Switchgear and Control Gear – General Rules; and</li>
        <li>AS3439.1 Low Voltage Switchgear and Control Gear Assemblies</li>
      </ul>
      <p>The tests performed included:</p>
      <ul>
        <li>Short Circuit Test;</li>
        <li>TCC Validation;</li>
        <li>Dielectric Tests;</li>
        <li>Temperature Rise; and</li>
        <li>Arc Fault Containment.</li>
      </ul>
    </section>
  </div>
</body>
</html>
```